Specialist Technical Theatre service for schools

The task is to design a brochure (A5, 4 pages) for mailing to secondary/high school heads and drama departments to sell them our services as Technical Theatre and Drama professionals who can help them to offer elements of a curriculum that they do not currently offer as well as raise the technical standards of their school productions.
Please find a document attached which outlines the content for the brochure. Please read the document first so that you understand our aims. The text highlighted in yellow takes priority - the text highlighted in blue could be used if there is space.
Photos which may be used available on https://www.pictaro.com/photos/ben_tovey/ (please do not use watermarked nordel images).
Logo is attached (two variants) - one of which should appear somewhere on the design. Website address is www.bentovey.co.uk and email is info@bentovey.co.uk
Target Market(s)
Theatre and Drama teachers in Secondary/High schools
Headteachers of Secondary/High Schools
Industry/Entity Type
Education
Look and feel

```html
<!DOCTYPE html>
<html lang="en">
<head>
<meta charset="utf-8">
<title>Ben Tovey – Technical Theatre Brochure Spread</title>
<link rel="stylesheet" href="https://fonts.googleapis.com/css2?family=Cherry+Swash:wght@400&family=Crimson+Text:wght@400;600&display=swap">
<style>
  :root{
    --yellow:#f6c630;
    --gold:#e9b93a;
    --ink:#070708;
    --night:#0c1527;
    --white:#f4f4f4;
    --muted:#a9a9ad;
    --rule:#4a4a4e;
    --backdrop:#e6e6e6;
    --brand-navy:#3c4677;
  }
  *{box-sizing:border-box;margin:0;padding:0}
  html,body{width:1200px;height:1000px;overflow:hidden}
  body{background:var(--backdrop);position:relative;font-family:"Crimson Text",Georgia,serif}

  .spread{position:absolute;left:60px;top:183px;width:1085px;height:755px;box-shadow:0 10px 24px rgba(0,0,0,.35)}
  .page{position:absolute;top:0;height:755px;overflow:hidden;background:var(--ink)}
  .page--back{left:0;width:545px}
  .page--front{left:545px;width:540px}

  .trim{position:absolute;left:0;top:0;width:100%;height:100%;pointer-events:none}

  /* back page */
  .photo{position:absolute}
  .photo--clowns{left:0;top:12px;width:545px;height:385px;
    background:radial-gradient(ellipse at 45% 25%,#8aa3c4 0%,#4d6a93 35%,#22334f 70%,#121a28 100%)}
  .roles{position:absolute;left:0;top:187px;width:545px;height:210px;background:rgba(5,6,10,.62);padding:10px 0 0 64px;color:var(--white)}
  .roles__title{font-size:16px;line-height:22px;color:var(--gold);margin-left:21px}
  .roles__list{list-style:none}
  .roles__list li{font-size:15px;line-height:21px;position:relative;padding-left:20px}
  .roles__list li::before{content:"";position:absolute;left:2px;top:7px;width:7px;height:7px;border:1.5px solid var(--yellow);transform:rotate(45deg)}
  .roles__list .note{color:var(--muted)}
  .roles__list li.roles__item--long{line-height:15px;padding-top:3px}
  .roles__list li.roles__item--long::before{top:8px}
  .roles__list .small{font-size:12px;line-height:14px}

  .criteria{position:absolute;top:418px;width:218px}
  .criteria--left{left:36px}
  .criteria--right{left:298px}
  .criterion{font-size:12px;line-height:13.5px;text-align:justify;padding:0 0 8px 0;margin-bottom:8px;border-bottom:1px solid var(--rule);position:relative}
  .criterion:last-child{border-bottom:none}
  .criterion::before{content:"";position:absolute;left:-12px;top:3px;width:6px;height:6px;border:1.3px solid currentColor;transform:rotate(45deg)}
  .criterion--gold{color:var(--gold)}
  .criterion--white{color:var(--white)}

  .badges{position:absolute;left:218px;top:682px;width:310px;height:44px}
  .badge{position:absolute}
  .badge--a{left:0;top:10px;width:64px;height:22px;background:#7b2f8f;border-radius:3px}
  .badge--b{left:92px;top:4px;width:22px;height:30px;background:#2c4a9a;border-radius:2px}
  .badge--c{left:193px;top:2px;width:38px;height:38px;background:#f2cc2a;border-radius:50%}
  .badge--d{left:250px;top:4px;width:58px;height:36px;background:#ffffff;border-radius:3px}

  /* front page */
  .photo--crowd{left:0;top:12px;width:540px;height:240px;
    background:radial-gradient(ellipse at 25% 10%,#c8d0dc 0%,#6c7787 18%,#2b323f 45%,#0d0f15 80%)}
  .brand{position:absolute;left:0;top:52px;width:540px;display:flex;align-items:center;justify-content:center;gap:12px}
  .brand__dot{width:30px;height:30px;border-radius:50%;background:var(--brand-navy)}
  .brand__name{font-size:28px;line-height:30px;color:#ffffff;font-weight:400}

  .headline{position:absolute;left:80px;top:240px;width:440px;transform:rotate(5deg);transform-origin:left top;color:var(--white);font-family:"Cherry Swash",Georgia,serif;font-weight:400;white-space:nowrap}
  .headline__lead{font-size:29px;line-height:32px;display:block}
  .headline__accent{font-size:27px;line-height:38px;color:var(--yellow);display:block;margin-left:38px}
  .headline__tail{font-size:26px;line-height:32px;display:block;margin-left:148px}

  .photo--dance{left:0;top:345px;width:540px;height:300px;
    background:radial-gradient(ellipse at 50% 30%,#d96ab0 0%,#9a3f9c 30%,#3a2a7a 60%,#141433 100%);
    clip-path:polygon(0 8%,100% 28%,100% 100%,0 100%)}

  .tagline{position:absolute;left:0;top:662px;width:540px;text-align:center;color:var(--gold);font-size:15.5px}
  .web{position:absolute;left:0;top:700px;width:540px;text-align:center;color:var(--yellow);font-size:25px;letter-spacing:.5px}
</style>
</head>
<body>
<main class="spread">

  <section class="page page--back" aria-label="Back page">
    <div class="photo photo--clowns" role="img" aria-label="Photo of costumed student dancers in clown hats reaching up on stage"></div>

    <div class="roles">
      <p class="roles__title">A GCSE or A-Level performance group can comprise of;</p>
      <ul class="roles__list">
        <li>Directing <span class="note">(one candidate per group)</span></li>
        <li>Acting <span class="note">(at least two candidates per group)</span></li>
        <li>Costume design <span class="note">(one candidate per group)</span></li>
        <li>Mask design <span class="note">(one candidate per group)</span></li>
        <li>Set design <span class="note">(one candidate per group)</span></li>
        <li class="roles__item--long">Technical elements: Lighting and/or Sound <span class="note small">(one candidate per element or one candidate assuming responsibility for both elements)</span></li>
      </ul>
    </div>

    <div class="criteria criteria--left">
      <p class="criterion criterion--gold">“Final lighting design incorporating grid plans and a lantern schedule that indicates the use of at least four different lighting states”</p>
      <p class="criterion criterion--white">“The student must supervise the production of the final sound design which they have created and recorded using live and/or sampled material as appropriate”</p>
      <p class="criterion criterion--gold">“Final costume designs for two characters in the production, incorporating hair, makeup and mask considerations if appropriate. All sourcing must be based wholly on the student’s design(s).”</p>
      <p class="criterion criterion--white">“Develop the ability to ensure colour gels, filters, gauzes, silhouettes, projections are used effectively”</p>
    </div>
    <div class="criteria criteria--right">
      <p class="criterion criterion--gold">“Develop the ability to ensure sound levels, reverb, echo, recorded sound effects, fades, soundscapes or music are manipulated effectively”</p>
      <p class="criterion criterion--white">“Develop the ability to select and exploit appropriate staging forms and to maximise the effectiveness of selected space, use of scale and levels, perspective; configuration of performer/ audience relationship”</p>
      <p class="criterion criterion--gold">And of course through all of the course detail it is repeated that we must “adopt the latest safe working practices.”</p>
    </div>

    <div class="badges" aria-label="Memberships and certificates">
      <span class="badge badge--a"></span>
      <span class="badge badge--b"></span>
      <span class="badge badge--c"></span>
      <span class="badge badge--d"></span>
    </div>

    <svg class="trim" viewBox="0 0 545 755" aria-hidden="true">
      <defs>
        <linearGradient id="fold" x1="0" x2="1"><stop offset="0" stop-color="#000" stop-opacity="0"/><stop offset="1" stop-color="#000" stop-opacity=".5"/></linearGradient>
      </defs>
      <polygon points="0,0 545,0 545,12 0,12" fill="#2a2417"/>
      <polygon points="0,0 270,0 0,45" fill="var(--yellow)"/>
      <polygon points="0,45 270,0 330,0 0,60" fill="#8a6a2c"/>
      <polygon points="0,755 0,728 300,755" fill="var(--yellow)"/>
      <polygon points="545,755 545,740 420,755" fill="var(--yellow)"/>
      <rect x="525" y="0" width="20" height="755" fill="url(#fold)"/>
    </svg>
  </section>

  <section class="page page--front" aria-label="Front page">
    <div class="photo photo--crowd" role="img" aria-label="Photo of a performing cast in silhouette under stage spotlights and haze"></div>

    <div class="brand">
      <span class="brand__dot"></span>
      <span class="brand__name">Ben Tovey</span>
    </div>

    <h1 class="headline">
      <span class="headline__lead">Want to bring</span>
      <span class="headline__accent">MORE ATTRACTION</span>
      <span class="headline__tail">to your theatre?</span>
    </h1>

    <div class="photo photo--dance" role="img" aria-label="Photo of a dancer mid-leap with cheerleaders under pink and blue stage lights"></div>

    <svg class="trim" viewBox="0 0 540 755" aria-hidden="true">
      <defs>
        <linearGradient id="foldR" x1="1" x2="0"><stop offset="0" stop-color="#000" stop-opacity="0"/><stop offset="1" stop-color="#000" stop-opacity=".5"/></linearGradient>
      </defs>
      <polygon points="0,0 540,0 540,12 0,12" fill="#2a2417"/>
      <polygon points="200,0 540,0 540,40" fill="var(--yellow)"/>
      <polygon points="0,369 540,429 540,422 0,362" fill="#2e4a7a"/>
      <rect x="0" y="645" width="540" height="110" fill="var(--night)"/>
      <polygon points="0,690 540,700 540,755 0,755" fill="var(--yellow)"/>
      <polygon points="0,695 540,706 540,748 0,748" fill="var(--ink)"/>
      <polygon points="0,755 0,700 120,755" fill="var(--yellow)"/>
      <polygon points="540,755 540,712 420,755" fill="var(--yellow)"/>
      <rect x="0" y="0" width="20" height="755" fill="url(#foldR)"/>
    </svg>

    <p class="tagline">School Technical Theatre support by Industry professionals.</p>
    <p class="web">www.bentovey.co.uk</p>
  </section>

</main>
</body>
</html>
```